New Business Cards for MB&LR

We need updated business cards for a staff of 15 engineers, estimators, project managers, and sales people. We have recently begun changes to our website and marketing material to improve our look and branding. We are an established fabricator specializing in pressure vessels, tanks, and structural steel. The owners require us to use the existing logo and old english text design. Also, we prefer dark grey or mostly black cards.
Target Market(s)
Engineers, purchasing agents, estimators, and project managers of; mining companies, refineries, industrial construction professionals
Industry/Entity Type
Business
Contact Information for Business Card
Logo, phone, website, email, etc.
Look and feel

```html
<!DOCTYPE html>
<html lang="en">
<head>
<meta charset="utf-8">
<title>MB&amp;LR Business Cards</title>
<link rel="stylesheet" href="https://fonts.googleapis.com/css2?family=Orbitron:wght@600&family=Jost:wght@300;400;500&family=Playfair+Display:wght@700&display=swap">
<style>
  :root {
    --backdrop: #3a3a3c;
    --card-black: #050505;
    --silver-light: #f4f5f6;
    --silver-mid: #b9bcc0;
    --silver-dark: #7d8288;
    --ink-dark: #111111;
    --ink-light: #ffffff;
    --ink-soft: #d6d6d6;
  }
  * { margin: 0; padding: 0; box-sizing: border-box; }
  html, body { width: 1200px; height: 782px; overflow: hidden; }
  body {
    background: var(--backdrop);
    font-family: "Jost", sans-serif;
    position: relative;
  }
  .card {
    position: absolute;
    width: 560px;
    height: 320px;
    background: var(--card-black);
    overflow: hidden;
    box-shadow: 0 10px 24px rgba(0,0,0,0.45);
  }
  .card-front { left: 40px; top: 60px; }
  .card-back { left: 600px; top: 400px; }
  .card-shapes { position: absolute; inset: 0; width: 100%; height: 100%; }

  .company-title {
    position: absolute;
    right: 26px;
    top: 26px;
    font-family: "Orbitron", sans-serif;
    font-weight: 600;
    font-size: 17px;
    letter-spacing: 0.5px;
    line-height: 1.25;
    text-align: right;
    color: var(--ink-dark);
  }
  .brand-mark {
    position: absolute;
    display: flex;
    align-items: center;
    gap: 8px;
    font-family: "Orbitron", sans-serif;
    font-weight: 600;
    color: var(--ink-dark);
  }
  .card-front .brand-mark { right: 40px; top: 108px; font-size: 20px; }
  .brand-square {
    width: 14px; height: 14px;
    background: var(--ink-dark);
  }
  .holder { position: absolute; left: 34px; top: 210px; color: var(--ink-light); }
  .holder-name { font-size: 19px; font-weight: 500; letter-spacing: 0.5px; }
  .holder-position { font-size: 15px; font-weight: 300; color: var(--ink-soft); margin-left: 90px; margin-top: -2px; }
  .contact-list {
    position: absolute;
    left: 30px;
    top: 264px;
    display: grid;
    grid-template-columns: auto auto;
    column-gap: 34px;
    row-gap: 6px;
    color: var(--ink-light);
    font-size: 17px;
  }
  .contact-item { display: flex; align-items: center; gap: 8px; }
  .contact-icon { width: 22px; height: 22px; flex: none; }

  .card-back .brand-block {
    position: absolute;
    left: 0; right: 0; top: 70px;
    text-align: center;
    color: var(--ink-dark);
  }
  .card-back .brand-name {
    font-family: "Orbitron", sans-serif;
    font-weight: 600;
    font-size: 30px;
  }
  .card-back .since {
    font-family: "Playfair Display", serif;
    font-weight: 700;
    font-size: 15px;
    margin-top: 10px;
  }
  .card-back .anniversary {
    font-family: "Playfair Display", serif;
    font-weight: 700;
    font-size: 22px;
    margin-top: 2px;
  }
  .website {
    position: absolute;
    left: 0; right: 0; bottom: 34px;
    text-align: center;
    color: var(--ink-light);
    font-size: 18px;
    letter-spacing: 0.5px;
  }
</style>
</head>
<body>

<section class="card card-front">
  <svg class="card-shapes" viewBox="0 0 560 320" aria-hidden="true">
    <defs>
      <linearGradient id="silverFront" x1="0" y1="0" x2="1" y2="0.3">
        <stop offset="0" stop-color="var(--silver-light)"/>
        <stop offset="0.55" stop-color="var(--silver-dark)"/>
        <stop offset="1" stop-color="var(--silver-mid)"/>
      </linearGradient>
    </defs>
    <path d="M0,0 H560 V110 Q560,128 544,136 L410,196 Q396,202 380,200 L0,128 Z" fill="url(#silverFront)"/>
    <path d="M0,82 L360,178 L380,200 L0,128 Z" fill="var(--silver-light)" opacity="0.9"/>
    <path d="M330,0 H560 V110 Q560,128 544,136 L470,170 Z" fill="var(--silver-light)" opacity="0.85"/>
  </svg>

  <h1 class="company-title">MIDLAND BEAM &amp; LOAD<br>RIGGING</h1>
  <div class="brand-mark"><span class="brand-square"></span>MB&amp;LR</div>

  <div class="holder">
    <div class="holder-name">HOLDER'S NAME</div>
    <div class="holder-position">Position</div>
  </div>

  <ul class="contact-list" style="list-style:none">
    <li class="contact-item">
      <svg class="contact-icon" viewBox="0 0 24 24"><circle cx="12" cy="12" r="12" fill="#fff"/><path d="M8 6.5l2 .2 1 2.8-1.3 1.1a7 7 0 0 0 3.7 3.7l1.1-1.3 2.8 1 .2 2c-.6 1-1.6 1.4-2.8 1.2A10 10 0 0 1 6.8 9.3C6.6 8.1 7 7.1 8 6.5z" fill="#000"/></svg>
      000-000-000
    </li>
    <li class="contact-item">
      <svg class="contact-icon" viewBox="0 0 24 24"><circle cx="12" cy="12" r="12" fill="#fff"/><path d="M12 5a5 5 0 0 0-5 5c0 4 5 9 5 9s5-5 5-9a5 5 0 0 0-5-5zm0 7a2 2 0 1 1 0-4 2 2 0 0 1 0 4z" fill="#000"/></svg>
      your address 3312
    </li>
    <li class="contact-item">
      <svg class="contact-icon" viewBox="0 0 24 24"><circle cx="12" cy="12" r="12" fill="#fff"/><rect x="6" y="8" width="12" height="8.5" rx="1" fill="#000"/><path d="M6.5 8.5l5.5 4.2 5.5-4.2" stroke="#fff" stroke-width="1.2" fill="none"/></svg>
      name@domain.com
    </li>
  </ul>
</section>

<section class="card card-back">
  <svg class="card-shapes" viewBox="0 0 560 320" aria-hidden="true">
    <defs>
      <linearGradient id="silverBack" x1="0" y1="0" x2="1" y2="0.4">
        <stop offset="0" stop-color="var(--silver-light)"/>
        <stop offset="0.6" stop-color="var(--silver-mid)"/>
        <stop offset="1" stop-color="var(--silver-dark)"/>
      </linearGradient>
    </defs>
    <path d="M150,0 H450 V190 Q450,212 428,214 L320,224 Q300,226 280,236 Q265,244 240,238 L176,226 Q150,220 150,196 Z" fill="url(#silverBack)"/>
  </svg>

  <div class="brand-block">
    <div class="brand-name">MB&amp;LR</div>
    <div class="since">1976</div>
    <div class="anniversary">40 YEARS</div>
  </div>

  <div class="website">www.mbandlr.com</div>
</section>

</body>
</html>
```